Unique Flyer Project - www.plumvaleforms.com.au

The purpose of this flyer is trying to get recipients to visit the website www.plumvaleforms.com.au and sign up to the offer. I need it to be simple/to the point, eye catching and professional. I will post up a basic idea I have but feel free to put your own spin on it if you think you have great ideas to get people to visit the site, if not then just improve upon the quality of mine and make it look like a respected company.

I also think a red band or something that REALLY catches the eye highlighting one of the important aspects of the flyer (the domain?) could be great so even if someone is about to put it in the bin, the popping red-on-white-background catches their eye so they end up looking at and reading the flyer.

I would also love a VERY SIMPLE design for the backside of the flyer, just a red box/band (whatever you think is good) with the domain 'www.plumvaleforms.com.au' in it. NOTHING ELSE! Just so if it's floating around the table and it's upside down, there's something eye catching that might entice the householder to look at it.

DESIGN IS FOR DL FLYER: 99mm X 210mm

Target Market(s)

Australian Residents interested in earning money from home.

Industry/Entity Type

It Company

Requirements
Must have
• Eye catching (mainly red band/box/bar on front & back page), SIMPLE, elegant/professional.
Should not have
• ANYTHING unnecessary to the reader that will distract them from the ultimate point - GET PAID TO DO SURVEYS FROM YOUR OWN HOME ON THE COMPUTER!

```html
<!DOCTYPE html>
<html lang="en">
<head>
<meta charset="utf-8">
<title>Plumvale Forms – DL Flyer, Front and Back</title>
<link href="https://fonts.googleapis.com/css2?family=Anton&family=Oswald:wght@600&family=Jost:wght@400&family=Arimo:wght@700&display=swap" rel="stylesheet">
<style>
  :root {
    --stage: #8c8c8c;
    --paper: #ffffff;
    --ink: #1c1c1c;
    --brand-red: #e8202a;
    --photo-light: #f2f2f2;
    --photo-mid: #d9d4cf;
    --photo-warm: #b98a70;
  }
  * { box-sizing: border-box; margin: 0; padding: 0; }
  html, body {
    width: 1200px;
    height: 1000px;
    overflow: hidden;
    background: var(--stage);
  }
  .stage {
    position: relative;
    width: 1200px;
    height: 1000px;
  }
  .flyer {
    position: absolute;
    top: 50px;
    width: 424px;
    height: 900px;
    background: var(--paper);
    overflow: hidden;
  }
  .flyer--front { left: 160px; }
  .flyer--back { left: 616px; }

  /* Front */
  .headline {
    position: absolute;
    top: 52px;
    left: 0;
    width: 100%;
    text-align: center;
    font-family: "Anton", sans-serif;
    font-size: 56px;
    line-height: 1.02;
    color: var(--ink);
    letter-spacing: 0.5px;
  }
  .subhead {
    position: absolute;
    top: 185px;
    left: 0;
    width: 100%;
    text-align: center;
    font-family: "Oswald", sans-serif;
    font-weight: 600;
    font-size: 25px;
    color: var(--brand-red);
    letter-spacing: 0.3px;
  }
  .hero-photo {
    position: absolute;
    top: 240px;
    left: 0;
    width: 100%;
    height: 500px;
    background:
      radial-gradient(ellipse 45% 55% at 50% 45%, var(--photo-warm) 0%, rgba(185,138,112,0) 70%),
      linear-gradient(180deg, var(--photo-light) 0%, var(--photo-mid) 100%);
  }
  .cta-band {
    position: absolute;
    left: 0;
    bottom: 0;
    width: 100%;
    height: 250px;
  }
  .cta-band svg { display: block; width: 100%; height: 100%; }
  .cta-line {
    position: absolute;
    bottom: 124px;
    left: 0;
    width: 100%;
    text-align: center;
    font-family: "Jost", sans-serif;
    font-size: 20px;
    color: var(--ink);
  }
  .domain-pill {
    position: absolute;
    bottom: 56px;
    left: 22px;
    right: 22px;
    height: 54px;
    border: 2px solid var(--paper);
    border-radius: 27px;
    display: flex;
    align-items: center;
    justify-content: center;
    font-family: "Arimo", sans-serif;
    font-weight: 700;
    font-size: 22px;
    color: var(--paper);
  }

  /* Back */
  .exclaim-bar {
    position: absolute;
    top: 240px;
    left: 183px;
    width: 58px;
    height: 440px;
    border-radius: 29px;
    background: var(--brand-red);
    display: flex;
    align-items: center;
    justify-content: center;
  }
  .exclaim-bar span {
    writing-mode: vertical-rl;
    transform: rotate(180deg);
    font-family: "Arimo", sans-serif;
    font-weight: 700;
    font-size: 25px;
    color: var(--paper);
    white-space: nowrap;
  }
  .exclaim-dot {
    position: absolute;
    top: 700px;
    left: 182px;
    width: 60px;
    height: 60px;
    border-radius: 50%;
    background: var(--brand-red);
  }
</style>
</head>
<body>
  <main class="stage">
    <section class="flyer flyer--front" aria-label="Flyer front">
      <h1 class="headline">START MAKING<br>CASH NOW!</h1>
      <p class="subhead">GET PAID FOR SURVEYS AT HOME</p>
      <div class="hero-photo" role="img" aria-label="Photo of a smiling woman at a laptop holding Australian banknotes"></div>
      <div class="cta-band">
        <svg viewBox="0 0 424 250" preserveAspectRatio="none" aria-hidden="true">
          <polygon points="0,48 424,0 424,250 0,250" fill="var(--brand-red)"/>
        </svg>
      </div>
      <p class="cta-line">Sign Up Now and Start Earning!</p>
      <p class="domain-pill">www.plumvaleforms.com.au</p>
    </section>

    <section class="flyer flyer--back" aria-label="Flyer back">
      <div class="exclaim-bar"><span>www.plumvaleforms.com.au</span></div>
      <div class="exclaim-dot"></div>
    </section>
  </main>
</body>
</html>
```